Velvet Oaks rebranding my business with a new business card

I have my new logo and now I need a refresher on my business cards. I really want something fun and fresh. I like black background or anything to make the color pop.
Logo
Name: Velvet Oaks
Contact Info as stated below:
Mira Calloway
647-382-9164
Logo
Name: Velvet Oaks
Mira Calloway
647-382-9164
fb.me/VelvetOaksbyMira
Instagram: @VelvetOaksbyMira

Industry/Entity Type

Business

Contact Information for Business Card

double-sided. Logo on one side. Contact info on the other.

Requirements
Must have
• Logo
• Name: Velvet Oaks
• Contact Info as stated below:
• Mira Calloway
• 647-382-9164
• fb.me/VelvetOaksbyMira
• fb.me/VelvetOaksbyMira

```html
<!DOCTYPE html>
<html lang="en">
<head>
<meta charset="utf-8">
<title>Velvet Oaks – Business Card</title>
<link rel="stylesheet" href="https://fonts.googleapis.com/css2?family=Roboto:wght@400;500&family=Roboto+Condensed:wght@700&display=swap">
<style>
  :root {
    --backdrop: #e9e4df;
    --pink: #f0a4b4;
    --pink-soft: #f5b9c6;
    --ink: #111111;
    --paper: #f1f1f1;
    --text: #4a4a4a;
    --url: #7b5e64;
    --white: #ffffff;
  }
  html, body {
    margin: 0;
    padding: 0;
    width: 1200px;
    height: 960px;
    overflow: hidden;
    background: var(--backdrop);
  }
  .canvas {
    position: relative;
    width: 1200px;
    height: 960px;
  }
  .card {
    position: absolute;
    left: 320px;
    width: 600px;
    height: 342px;
    border-radius: 16px;
    overflow: hidden;
    box-shadow: 0 4px 10px rgba(0,0,0,0.25);
  }
  .card-front {
    top: 100px;
    background: var(--pink);
  }
  .front-brand {
    position: absolute;
    left: 0;
    right: 0;
    top: 150px;
    text-align: center;
    font-family: "Roboto", sans-serif;
    font-weight: 500;
    font-size: 30px;
    letter-spacing: 3px;
    color: var(--ink);
    text-transform: uppercase;
  }
  .front-url {
    position: absolute;
    left: 0;
    right: 0;
    top: 298px;
    text-align: center;
    font-family: "Roboto", sans-serif;
    font-size: 14px;
    letter-spacing: 6px;
    color: var(--url);
  }
  .card-back {
    top: 493px;
    background: var(--paper);
  }
  .back-wave {
    position: absolute;
    left: 0;
    top: 0;
  }
  .holder-name {
    position: absolute;
    right: 52px;
    top: 30px;
    font-family: "Roboto Condensed", sans-serif;
    font-weight: 700;
    font-size: 21px;
    color: var(--white);
    text-transform: uppercase;
  }
  .brand-seal {
    position: absolute;
    left: 90px;
    top: 170px;
    width: 120px;
    height: 120px;
    border-radius: 50%;
    background: var(--white);
    border: 2px solid var(--pink);
    box-shadow: 0 0 0 4px var(--white), 0 0 0 5px var(--pink);
    display: flex;
    align-items: center;
    justify-content: center;
    text-align: center;
    font-family: "Roboto", sans-serif;
    font-weight: 500;
    font-size: 15px;
    line-height: 1.2;
    letter-spacing: 1px;
    color: var(--ink);
    text-transform: uppercase;
  }
  .divider {
    position: absolute;
    left: 280px;
    top: 195px;
    width: 1px;
    height: 88px;
    background: #9a9a9a;
  }
  .contact-list {
    position: absolute;
    left: 307px;
    top: 208px;
    margin: 0;
    padding: 0;
    list-style: none;
    font-family: "Roboto", sans-serif;
    font-size: 14px;
    color: var(--text);
  }
  .contact-list li {
    display: flex;
    align-items: center;
    height: 19px;
  }
  .contact-icon {
    width: 12px;
    height: 12px;
    margin-right: 9px;
    flex: none;
  }
  .square-mark {
    width: 10px;
    height: 10px;
    margin: 0 10px 0 1px;
    background: #333;
    flex: none;
  }
</style>
</head>
<body>
<main class="canvas">
  <section class="card card-front" aria-label="Card front">
    <div class="front-brand">Velvet Oaks</div>
    <div class="front-url">www.velvetoaks.com</div>
  </section>

  <section class="card card-back" aria-label="Card back">
    <svg class="back-wave" width="600" height="342" viewBox="0 0 600 342" aria-hidden="true">
      <path d="M0,95 C120,55 230,60 330,95 C430,130 530,130 600,75 L600,110 C520,150 420,150 320,120 C210,90 110,100 0,170 Z" fill="var(--pink-soft)"/>
      <path d="M0,100 C120,60 230,62 330,100 C430,138 540,135 600,80 L600,100 C540,150 430,152 330,118 C230,86 120,80 0,120 Z" fill="var(--paper)"/>
      <path d="M0,0 H600 V70 C540,118 440,122 350,98 C250,70 160,50 0,88 Z" fill="var(--ink)"/>
      <path d="M0,88 C160,50 250,70 350,98 C440,122 540,118 600,70 V85 C540,132 440,136 350,112 C250,84 160,66 0,100 Z" fill="var(--white)"/>
      <path d="M280,108 C360,128 450,140 520,128 C560,120 585,105 600,92 V100 C575,122 540,135 500,140 C420,148 350,132 280,108 Z" fill="var(--ink)"/>
    </svg>
    <div class="holder-name">Mira Calloway</div>
    <div class="brand-seal">Velvet<br>Oaks</div>
    <div class="divider"></div>
    <ul class="contact-list">
      <li>
        <svg class="contact-icon" viewBox="0 0 24 24" aria-hidden="true"><path fill="#333" d="M6.6 10.8a15.1 15.1 0 0 0 6.6 6.6l2.2-2.2c.3-.3.7-.4 1-.2 1.1.4 2.3.6 3.6.6.6 0 1 .4 1 1V20c0 .6-.4 1-1 1C10.6 21 3 13.4 3 4c0-.6.4-1 1-1h3.5c.6 0 1 .4 1 1 0 1.2.2 2.4.6 3.6.1.3 0 .7-.2 1z"/></svg>
        647-382-9164
      </li>
      <li>
        <svg class="contact-icon" viewBox="0 0 24 24" aria-hidden="true"><circle cx="12" cy="12" r="10" fill="none" stroke="#333" stroke-width="2.5"/><path d="M2 12h20M12 2c3 3 3 17 0 20M12 2c-3 3-3 17 0 20" fill="none" stroke="#333" stroke-width="2"/></svg>
        www.velvetoaks.com
      </li>
      <li>
        <span class="square-mark" aria-hidden="true"></span>
        fb.me/VelvetOaksbyMira
      </li>
    </ul>
  </section>
</main>
</body>
</html>
```